Brindle Microdevices Core Values Posters + Icons

Interested in helping us refresh our core values posters? Click on the attached document for more details! (review brindlemicro.example for more information about Brindle)

Deliverables are the following:
o 6 Core Value Posters – each shows the core value and the statement that accompanies that value (e.g. “Accountability” and “We keep our Promises.”) and smaller representations of the other 5 values (see concept sketch)
o 6 Core Value icons – an image that demonstrates the core value that can be placed large on each poster and repurposed on things like coasters and awards.
Updates

Reason: There are some great designs being submitted and they still need a bit more work. Have an idea? Submit yours now!

Target Market(s)

Employees of Brindle Microdevices Worldwide

Font styles to use
Sans Serif

Requirements
Must have
• Must have:
• Core Values and We Statements
• Icon Associated with each Core Value
• Clean design with strong emphasis on the featured core value/we statement pair
Nice to have
• Must make sense globally

```html
<!DOCTYPE html>
<html lang="en">
<head>
<meta charset="utf-8">
<title>Brindle Microdevices – Accountability</title>
<link rel="stylesheet" href="https://fonts.googleapis.com/css2?family=Roboto+Condensed:wght@700&display=swap">
<style>
  :root {
    --paper: #ffffff;
    --gold-center: #f0ba08;
    --gold-mid: #d69a12;
    --rust-edge: #a4562a;
    --rust-corner: #8f3f2c;
    --ink: #0b0b0b;
    --white: #ffffff;
    --accent: #f8c21c;
  }
  * { margin: 0; padding: 0; box-sizing: border-box; }
  html, body { width: 960px; height: 1200px; overflow: hidden; background: var(--paper); }
  body { font-family: "Roboto Condensed", "Arial Narrow", sans-serif; }
  .canvas { position: relative; width: 960px; height: 1200px; background: var(--paper); }
  .poster {
    position: absolute; left: 40px; top: 40px; width: 880px; height: 1120px;
    background: radial-gradient(ellipse 75% 70% at 50% 50%, var(--gold-center) 0%, var(--gold-mid) 55%, var(--rust-edge) 90%, var(--rust-corner) 110%);
    overflow: hidden;
  }
  .values-row { position: absolute; top: 36px; left: 0; width: 100%; height: 120px; }
  .value { position: absolute; width: 150px; margin-left: -75px; text-align: center; color: var(--white); }
  .value svg { display: block; margin: 0 auto; width: 80px; height: 80px; }
  .value-label { display: block; margin-top: 6px; font-size: 14px; letter-spacing: 0.2px; }
  .hero-icon { position: absolute; left: 268px; top: 332px; width: 344px; height: 336px; }
  .hero-shadow {
    position: absolute; left: 336px; top: 690px; width: 208px; height: 12px; border-radius: 50%;
    background: radial-gradient(ellipse at center, rgba(40,25,0,0.55), rgba(40,25,0,0) 70%);
  }
  .value-title {
    position: absolute; top: 862px; left: 0; width: 100%; text-align: center;
    color: var(--white); font-size: 93px; line-height: 1; letter-spacing: 1px;
  }
  .value-statement {
    position: absolute; top: 945px; left: 0; width: 100%; text-align: center;
    color: var(--white); font-size: 52px; line-height: 1;
  }
  .brand {
    position: absolute; top: 1012px; left: 0; width: 100%;
    display: flex; justify-content: center; align-items: center; gap: 12px;
  }
  .brand-square { width: 40px; height: 40px; background: var(--accent); }
  .brand-name { color: var(--ink); font-size: 46px; line-height: 1; letter-spacing: 1px; text-transform: uppercase; }
  .tagline {
    position: absolute; top: 1090px; left: 0; width: 100%; text-align: center;
    color: var(--accent); font-size: 29.5px; line-height: 1;
  }
</style>
</head>
<body>
<div class="canvas">
  <main class="poster">
    <ul class="values-row" style="list-style:none">
      <li class="value" style="left:172px">
        <svg viewBox="0 0 80 80" aria-hidden="true">
          <path d="M28 50 L18 74 L27 70 L31 78 L38 56Z M52 50 L62 74 L53 70 L49 78 L42 56Z" fill="var(--white)"/>
          <circle cx="40" cy="32" r="24" fill="var(--white)"/>
          <circle cx="40" cy="32" r="14" fill="var(--gold-mid)"/>
          <polygon points="40,22 43,29 50,30 45,35 46,42 40,38 34,42 35,35 30,30 37,29" fill="var(--white)"/>
        </svg>
        <span class="value-label">CUSTOMER OBSESSION</span>
      </li>
      <li class="value" style="left:344px">
        <svg viewBox="0 0 80 80" aria-hidden="true">
          <circle cx="40" cy="28" r="9" fill="var(--white)"/>
          <circle cx="22" cy="34" r="6" fill="var(--white)"/>
          <circle cx="58" cy="34" r="6" fill="var(--white)"/>
          <circle cx="9" cy="38" r="5" fill="var(--white)"/>
          <circle cx="71" cy="38" r="5" fill="var(--white)"/>
          <path d="M24 56 Q40 34 56 56Z M8 54 Q22 38 34 52Z M46 52 Q58 38 72 54Z" fill="var(--white)"/>
        </svg>
        <span class="value-label">TEAMWORK</span>
      </li>
      <li class="value" style="left:502px">
        <svg viewBox="0 0 80 80" aria-hidden="true">
          <rect x="40" y="12" width="10" height="6" fill="var(--white)"/>
          <circle cx="45" cy="44" r="22" fill="var(--white)"/>
          <circle cx="45" cy="44" r="16" fill="var(--gold-mid)"/>
          <line x1="45" y1="44" x2="45" y2="32" stroke="var(--white)" stroke-width="3"/>
          <path d="M4 40 L22 38 L20 44Z M8 50 L22 48 L22 54Z" fill="var(--white)"/>
        </svg>
        <span class="value-label">SPEED</span>
      </li>
      <li class="value" style="left:626px">
        <svg viewBox="0 0 80 80" aria-hidden="true">
          <g stroke="#d9d9d9" stroke-width="2">
            <line x1="40" y1="4" x2="40" y2="76"/><line x1="4" y1="40" x2="76" y2="40"/>
            <line x1="14" y1="14" x2="66" y2="66"/><line x1="66" y1="14" x2="14" y2="66"/>
          </g>
          <circle cx="40" cy="40" r="20" fill="var(--white)"/>
          <circle cx="40" cy="40" r="11" fill="#c8c8c8"/>
        </svg>
        <span class="value-label">INNOVATION</span>
      </li>
      <li class="value" style="left:752px">
        <svg viewBox="0 0 80 80" aria-hidden="true">
          <circle cx="44" cy="50" r="18" fill="none" stroke="var(--white)" stroke-width="9"/>
          <path d="M26 50 L26 10 L35 6 L35 46Z" fill="var(--white)"/>
        </svg>
        <span class="value-label">QUALITY</span>
      </li>
    </ul>

    <svg class="hero-icon" viewBox="0 0 344 336" role="img" aria-label="Core value icon: a target with an arrow in its centre">
      <ellipse cx="172" cy="168" rx="168" ry="164" fill="var(--ink)"/>
    </svg>
    <div class="hero-shadow"></div>

    <h1 class="value-title">ACCOUNTABILITY</h1>
    <p class="value-statement">We keep our promises.</p>

    <div class="brand">
      <span class="brand-square"></span>
      <span class="brand-name">Brindle Microdevices</span>
    </div>

    <p class="tagline">Accelerating customer innovation for a better connected world</p>
  </main>
</div>
</body>
</html>
```